Tech Website

1. Overview
Lumora9, formally named VantaSight, is a pioneer in computer vision technology and machine learning. Based out of Santa Clara, California, Lumora9 is at the forefront of the User Interface revolution; building technology architecture that grants devices with the aptitude to respond to emotional detection, gaze tracking, facial recognition, age and gender identification and gaming interaction. Winner of the Mobile Track at BRISK Founders Sprint 2012, Lumora9 has developed the next generation of consumer behaviour analytics. Lumora9 software solutions are scalable across various platforms including mobile phone, tablets, PC and SmartTV.
Updates

Good day, 

Please see the update to our brief - there is a PDF of the type of format and design we are looking for.  It shows each page - Landing, Technology, Product, Press and Company.

Thank you for your designs

Regards,

Target Market(s)

Target market - A mix of enterprise and consumer audiences, targeting the need for the technology in the living room space

Industry/Entity Type

Architecture

Requirements
Must have
• Design preferences - Easy to navigate, modern with sleek feel, trendy, tech saavy, using cube as a consistent element/theme. colours are not determined, but parrot green was one idea with 2 additional underlying colours. keys words like user interface revolution or sense recognition are good sources to draw inspiration.

Landing page will have a video - illustrating different uses of technology

Technical Specs - Landing page, 6 tabs/subpages, and each subpage may have 1 or 2 additional pages. Coding will be necessary, not that much at the beginning stages.

```html
<!DOCTYPE html>
<html lang="en">
<head>
<meta charset="utf-8">
<title>Lumora9 – Computer Vision Technology</title>
<link href="https://fonts.googleapis.com/css2?family=Play:wght@400;700&family=Ubuntu:wght@400;500;700&family=Cabin:wght@400;600&display=swap" rel="stylesheet">
<style>
:root{
  --green:#8aab0a;
  --green-dark:#6f8c05;
  --header-top:#3a3a3a;
  --header-bottom:#151515;
  --hero-top:#f7f7f7;
  --hero-bottom:#e4e4e4;
  --ink:#1c1c1c;
  --body-text:#444;
  --muted:#888;
  --rule:#cfcfcf;
  --white:#fff;
  --black:#000;
  --blue:#2a7fd0;
  --blue-dark:#1d63aa;
  --icon:#5a5a5a;
}
*{box-sizing:border-box;margin:0;padding:0}
html,body{width:1200px;height:971px;overflow:hidden}
body{position:relative;background:var(--white);font-family:"Cabin",sans-serif;color:var(--ink)}
.abs{position:absolute}

/* header */
.site-header{left:0;top:0;width:1200px;height:80px;background:linear-gradient(var(--header-top),var(--header-bottom))}
.brand{left:120px;top:2px;width:252px;height:91px;background:var(--white);border-radius:3px;box-shadow:0 6px 10px rgba(0,0,0,.25);z-index:3;display:flex;align-items:center}
.brand-mark{width:58px;height:56px;margin-left:8px;background:var(--green);border:2px solid var(--green-dark)}
.brand-name{margin-left:20px;font-family:"Play",sans-serif;font-size:36px;color:#333}
.main-nav{left:589px;top:0;height:80px;display:flex}
.main-nav a{display:block;height:80px;line-height:96px;padding:0 17px;font-family:"Ubuntu",sans-serif;font-size:16px;color:var(--white);text-decoration:none;margin-right:9px}
.main-nav a.active{background:var(--green);padding:0 12px;margin-right:22px}

/* hero */
.hero{left:0;top:80px;width:1200px;height:453px;background:linear-gradient(var(--hero-top),var(--hero-bottom))}
.frame{background:var(--white);box-shadow:0 2px 6px rgba(0,0,0,.3)}
.frame-back{left:125px;top:158px;width:558px;height:293px}
.frame-back .still{position:absolute;left:11px;top:11px;right:11px;bottom:11px;background:linear-gradient(90deg,#c9ccd2,#e8e9ec 50%,#c9ccd2)}
.frame-front{left:156px;top:142px;width:498px;height:325px}
.video-still{position:absolute;left:11px;top:11px;width:476px;height:275px;background:linear-gradient(135deg,#d9c2ae 0%,#c9cfd9 35%,#e9ecf2 60%,#2c2c2c 100%)}
.play-big{position:absolute;left:193px;top:87px;width:100px;height:100px;border-radius:50%;background:rgba(90,90,90,.75)}
.controls{position:absolute;background:#111;display:flex;align-items:center;color:#ddd;font-family:"Ubuntu",sans-serif}
.controls-main{left:11px;top:286px;width:476px;height:28px;font-size:8px}
.controls-main .time{margin:0 8px}
.track{flex:1;height:4px;background:#444;position:relative}
.track i{position:absolute;left:0;top:0;height:4px;background:#5fc01d}
.hero-title{left:718px;top:152px;font-family:"Play",sans-serif;font-size:30px;color:var(--black);text-shadow:0 2px 3px rgba(0,0,0,.25)}
.hero-copy{left:720px;top:208px;width:350px;font-size:13.5px;line-height:20px;color:var(--body-text);text-align:justify}
.hero-copy p+p{margin-top:20px}
.btn-more{left:721px;top:405px;width:154px;height:44px;border:1px solid #bbb;border-radius:3px;background:linear-gradient(#fff,#dcdcdc);box-shadow:0 2px 4px rgba(0,0,0,.3);font-family:"Ubuntu",sans-serif;font-size:21px;color:#333;text-align:center;line-height:44px}

/* feature videos */
.clip{top:559px;width:212px;height:178px;background:#111}
.clip-title{height:26px;line-height:26px;padding-left:7px;font-family:"Ubuntu",sans-serif;font-size:13px;color:var(--white)}
.clip-still{position:relative;height:135px}
.clip-still .play{position:absolute;left:86px;top:43px;width:40px;height:40px;border-radius:50%;background:rgba(70,70,70,.8)}
.clip .controls{position:static;height:17px;padding:0 6px}
.clip .track{height:3px;margin-left:30px;margin-right:14px}
.clip .track i{height:3px}

/* sidebar */
.join{left:822px;top:559px;width:250px;height:59px;background:linear-gradient(#95b60f,#759507);box-shadow:0 2px 3px rgba(0,0,0,.25);color:var(--white)}
.join-divider{position:absolute;left:56px;top:10px;width:1px;height:38px;background:rgba(255,255,255,.4)}
.join-title{position:absolute;left:75px;top:9px;font-family:"Ubuntu",sans-serif;font-weight:700;font-size:18px}
.join-date{position:absolute;left:75px;top:33px;font-family:"Ubuntu",sans-serif;font-size:12px}
.subscribe-title{left:820px;top:641px;font-family:"Ubuntu",sans-serif;font-size:18px;color:var(--black)}
.subscribe-hint{left:821px;top:672px;font-size:13px;color:var(--muted)}
.subscribe-field{left:820px;top:698px;width:252px;height:40px;border:1px solid #bbb;border-radius:5px;background:var(--white)}
.subscribe-field span{position:absolute;left:10px;top:12px;font-size:11px;color:var(--muted)}
.subscribe-btn{position:absolute;left:160px;top:3px;width:85px;height:32px;border-radius:4px;background:linear-gradient(#3b93e0,var(--blue-dark));border:1px solid #17508a;color:#0d2f55;font-family:"Ubuntu",sans-serif;font-size:12px;font-weight:500;text-align:center;line-height:30px}

/* featured */
.featured-rule{top:793px;height:1px;background:var(--rule)}
.featured-title{left:514px;width:173px;top:778px;text-align:center;font-family:"Ubuntu",sans-serif;font-size:20px;color:#555}
.press-row{left:128px;top:828px;width:946px;display:flex;justify-content:space-between;align-items:center;font-family:"Cabin",sans-serif;font-weight:600;font-size:30px;color:#333}
.press-row span{width:185px;text-align:center}

/* footer */
.site-footer{left:0;top:912px;width:1200px;height:59px;background:var(--black)}
.footer-nav{position:absolute;left:139px;top:20px;font-family:"Ubuntu",sans-serif;font-size:14px;color:var(--white)}
.footer-nav .sep{margin:0 10px}
.social{position:absolute;left:859px;top:18px}
</style>
</head>
<body>

<header class="site-header abs">
  <nav class="main-nav abs">
    <a class="active" href="#">Home</a>
    <a href="#">Technology</a>
    <a href="#">Product</a>
    <a href="#">Press</a>
    <a href="#">Company</a>
  </nav>
</header>
<div class="brand abs"><div class="brand-mark"></div><span class="brand-name">Lumora9</span></div>

<section class="hero abs"></section>
<div class="frame frame-back abs"><div class="still" role="img" aria-label="Second video still in the carousel"></div></div>
<div class="frame frame-front abs">
  <div class="video-still" role="img" aria-label="Video still: a hand touching a tablet showing a business news page">
    <div class="play-big"><svg width="100" height="100" viewBox="0 0 100 100"><path d="M38 28 L74 50 L38 72 Z" fill="#fff"/></svg></div>
  </div>
  <div class="controls controls-main">
    <svg width="30" height="28" viewBox="0 0 30 28"><path d="M12 9 L20 14 L12 19 Z" fill="#fff"/></svg>
    <span class="time">00:26</span>
    <div class="track"><i style="width:57%"></i></div>
    <span class="time">00:35</span>
    <svg width="44" height="28" viewBox="0 0 44 28"><path d="M2 11h3l4-3v12l-4-3H2z" fill="#fff"/><rect x="13" y="12" width="28" height="3" fill="#444"/><rect x="13" y="12" width="18" height="3" fill="#5fc01d"/></svg>
    <svg width="30" height="28" viewBox="0 0 30 28" fill="#fff"><path d="M9 8h4v1.5h-2.5V12H9zM21 8h-4v1.5h2.5V12H21zM9 20h4v-1.5h-2.5V16H9zM21 20h-4v-1.5h2.5V16H21z"/></svg>
  </div>
</div>

<h1 class="hero-title abs">Welcome to Lumora9</h1>
<div class="hero-copy abs">
  <p>Sed gravida nunc at erat tincidunt iaculis. Nam ac orci diam, sit amet commodo leo. Phasellus consequat augue sed arcu volutpat lobortis vel nec justo. Nunc faucibus laoreet orci ut tristique.</p>
  <p>Duis a quam ut neque mollis imperdiet a a lacus. Integer quis diam nunc, eu aliquet nibh. Sed venenatis.Duis a quam ut neque mollis imperdiet a a lacus. Integer quis diam nunc, eu aliquet nibh. Sed venenatis.</p>
</div>
<div class="btn-more abs">Read More</div>

<div class="clip abs" style="left:128px">
  <div class="clip-title">Media Database</div>
  <div class="clip-still" role="img" aria-label="Presenter pointing at a large wall map" style="background:linear-gradient(90deg,#9aa6a8,#b9a58c 50%,#8e9aa6)"><div class="play"><svg width="40" height="40" viewBox="0 0 40 40"><path d="M15 11 L29 20 L15 29 Z" fill="#fff"/></svg></div></div>
  <div class="controls"><svg width="8" height="8" viewBox="0 0 8 8"><path d="M1 0L7 4L1 8Z" fill="#fff"/></svg><div class="track"><i style="width:55%"></i></div></div>
</div>
<div class="clip abs" style="left:354px">
  <div class="clip-title">Technology</div>
  <div class="clip-still" role="img" aria-label="Person holding a tablet with floating app windows" style="background:linear-gradient(90deg,#c8ccd3,#eef0f3 55%,#d6d9de)"><div class="play"><svg width="40" height="40" viewBox="0 0 40 40"><path d="M15 11 L29 20 L15 29 Z" fill="#fff"/></svg></div></div>
  <div class="controls"><svg width="8" height="8" viewBox="0 0 8 8"><path d="M1 0L7 4L1 8Z" fill="#fff"/></svg><div class="track"><i style="width:55%"></i></div></div>
</div>
<div class="clip abs" style="left:579px">
  <div class="clip-title">Products</div>
  <div class="clip-still" role="img" aria-label="Business meeting around a tablet showing charts" style="background:linear-gradient(135deg,#7d93ad,#c9d3de 50%,#e7ecf1)"><div class="play"><svg width="40" height="40" viewBox="0 0 40 40"><path d="M15 11 L29 20 L15 29 Z" fill="#fff"/></svg></div></div>
  <div class="controls"><svg width="8" height="8" viewBox="0 0 8 8"><path d="M1 0L7 4L1 8Z" fill="#fff"/></svg><div class="track"><i style="width:55%"></i></div></div>
</div>

<div class="join abs">
  <svg class="abs" style="left:20px;top:20px" width="20" height="20" viewBox="0 0 20 20" fill="none" stroke="#fff" stroke-width="3"><path d="M3 3l7 7-7 7M10 3l7 7-7 7"/></svg>
  <div class="join-divider"></div>
  <div class="join-title">Join Us At</div>
  <div class="join-date">NEXA Expo 2013 Jan 8-11</div>
</div>
<h2 class="subscribe-title abs">Subscribe to Lumora9 Blog</h2>
<div class="subscribe-hint abs">Enter your email address.</div>
<div class="subscribe-field abs"><span>Your email address...</span><div class="subscribe-btn">Subscribe</div></div>

<div class="featured-rule abs" style="left:128px;width:386px"></div>
<div class="featured-rule abs" style="left:687px;width:387px"></div>
<h3 class="featured-title abs">As Featured In</h3>
<div class="press-row abs">
  <span>Novaline</span>
  <span>Qubit Daily</span>
  <span>Brightwire</span>
  <span>Orbis</span>
  <span>Signal Review</span>
</div>

<footer class="site-footer abs">
  <div class="footer-nav">Home<span class="sep">|</span>Technology<span class="sep">|</span>Product<span class="sep">|</span>Press<span class="sep">|</span>Company</div>
  <svg class="social" width="210" height="24" viewBox="0 0 210 24" fill="var(--icon)">
    <circle cx="12" cy="12" r="11"/><circle cx="42" cy="12" r="11"/><circle cx="72" cy="12" r="11"/><circle cx="102" cy="12" r="11"/><circle cx="132" cy="12" r="11"/><circle cx="162" cy="12" r="11"/><circle cx="192" cy="12" r="11"/>
  </svg>
</footer>

</body>
</html>
```